New Business Card Design Project

Details for my new Business Card Design Project will be added soon. Like a nice simple design

Target Market(s)

Home improvement

Industry/Entity Type

Home Improvement

Contact Information for Business Card

Roofing siding gutters additions garages decks

Requirements
Must have
• Phone 5097362418
• Email korvandpm@mailnest.net

```html
<!DOCTYPE html>
<html lang="en">
<head>
<meta charset="utf-8">
<title>Korvand Home Works – Business Card</title>
<link rel="stylesheet" href="https://fonts.googleapis.com/css2?family=Arimo:wght@400;700&display=swap">
<style>
  :root {
    --navy: #1a1150;
    --red: #ec1c24;
    --white: #ffffff;
    --backdrop: #e6e6e8;
  }
  * { margin: 0; padding: 0; box-sizing: border-box; }
  html, body {
    width: 1200px;
    height: 1000px;
    overflow: hidden;
    background: var(--backdrop);
    font-family: "Arimo", Arial, sans-serif;
  }
  .card {
    position: absolute;
    left: 50px;
    top: 160px;
    width: 1100px;
    height: 680px;
    background: var(--navy);
    color: var(--white);
  }
  .brand {
    position: absolute;
    left: 0;
    right: 0;
    top: 70px;
    display: flex;
    flex-direction: column;
    align-items: center;
    gap: 22px;
  }
  .brand-square {
    width: 56px;
    height: 56px;
    background: var(--red);
  }
  .brand-name {
    font-weight: 700;
    font-size: 44px;
    letter-spacing: 0.5px;
    color: var(--white);
  }
  .services {
    position: absolute;
    left: 0;
    right: 0;
    display: flex;
    justify-content: center;
    align-items: center;
    font-weight: 700;
    font-size: 37px;
    line-height: 1;
  }
  .services-primary { top: 327px; }
  .services-secondary { top: 398px; }
  .service + .service {
    border-left: 2px solid var(--white);
    margin-left: 14px;
    padding-left: 14px;
  }
  .services-secondary .service + .service {
    margin-left: 30px;
    padding-left: 30px;
  }
  .divider {
    position: absolute;
    left: 0;
    right: 0;
    top: 475px;
    height: 4px;
    background: var(--red);
  }
  .contact {
    position: absolute;
    left: 0;
    right: 0;
    top: 506px;
    text-align: center;
    font-weight: 700;
  }
  .contact-phone { font-size: 37px; line-height: 1.1; }
  .contact-email { font-size: 28px; line-height: 1.1; margin-top: 8px; }
</style>
</head>
<body>
  <section class="card">
    <div class="brand">
      <div class="brand-square"></div>
      <div class="brand-name">Korvand Home Works</div>
    </div>

    <div class="services services-primary">
      <span class="service">Roofing</span>
      <span class="service">Siding</span>
      <span class="service">Gutter</span>
      <span class="service">Additions</span>
    </div>
    <div class="services services-secondary">
      <span class="service">Decks</span>
      <span class="service">Handyman Services</span>
    </div>

    <div class="divider"></div>

    <div class="contact">
      <p class="contact-phone">Ph: 509-736-2418</p>
      <p class="contact-email">korvandpm@mailnest.net</p>
    </div>
  </section>
</body>
</html>
```